Brightwire Hollow Business cards

one side I would like my logo (uploaded) and the other side I want my details. I'm an electrician in sydney. The logo side I'm happy with just a white background and our logo in the middle.

Details for other side
24/7 Sydney Electrician
Marcus Pell
0431 587 219
marcus@brightwirehollow.com.au
brightwirehollow.com.au
icons for facebook, instagram, linked in

Industry/Entity Type

electrician

Contact Information for Business Card

company info

```html
<!DOCTYPE html>
<html lang="en">
<head>
<meta charset="utf-8">
<title>Brightwire Hollow – Business Cards</title>
<link rel="stylesheet" href="https://fonts.googleapis.com/css2?family=Michroma&family=Lexend:wght@400;500;600&display=swap">
<style>
  :root {
    --page-bg: #e4e3e1;
    --card-white: #ffffff;
    --card-black: #1d1c1c;
    --brand-red: #e8321f;
    --ink-black: #141414;
    --text-light: #f2f2f2;
    --band-red: #6b2a1e;
  }
  * { box-sizing: border-box; margin: 0; padding: 0; }
  html, body { width: 1200px; height: 895px; overflow: hidden; }
  body {
    background: var(--page-bg);
    font-family: "Lexend", sans-serif;
    position: relative;
  }
  .card {
    position: absolute;
    top: 288px;
    width: 520px;
    height: 318px;
    border-radius: 22px;
    overflow: hidden;
    box-shadow: 0 6px 18px rgba(0,0,0,0.18);
  }
  /* Front: logo side */
  .card--front {
    left: 50px;
    background: var(--card-white);
    display: flex;
    align-items: center;
    justify-content: center;
  }
  .brand-name {
    font-family: "Michroma", sans-serif;
    font-size: 30px;
    line-height: 1.25;
    color: var(--brand-red);
    text-transform: uppercase;
    text-align: center;
    letter-spacing: 1px;
  }
  /* Back: details side */
  .card--back {
    left: 630px;
    background: var(--card-black);
    color: var(--text-light);
  }
  .corner-accent {
    position: absolute;
    right: 0;
    top: 150px;
    width: 6px;
    height: 40px;
    background: var(--brand-red);
  }
  .holder-name {
    position: absolute;
    left: 30px;
    top: 108px;
    width: 200px;
    font-family: "Michroma", sans-serif;
    font-size: 21px;
    line-height: 1.1;
    color: var(--brand-red);
    text-transform: uppercase;
    text-align: right;
    white-space: nowrap;
    direction: ltr;
  }
  .divider {
    position: absolute;
    left: 250px;
    top: 72px;
    width: 2px;
    height: 100px;
    background: var(--text-light);
  }
  .contact-list {
    position: absolute;
    left: 266px;
    top: 78px;
    list-style: none;
  }
  .contact-item {
    display: flex;
    align-items: center;
    gap: 8px;
    height: 30px;
    font-size: 12px;
    font-weight: 500;
    letter-spacing: 0.3px;
    white-space: nowrap;
  }
  .contact-item--phone { font-size: 16px; font-weight: 600; }
  .contact-icon { width: 14px; height: 14px; flex: none; }
  .tagline-band {
    position: absolute;
    left: 0;
    right: 0;
    top: 218px;
    height: 30px;
    background: linear-gradient(90deg, rgba(107,42,30,0) 0%, var(--band-red) 45%, rgba(107,42,30,0.6) 75%, rgba(107,42,30,0) 100%);
    display: flex;
    align-items: center;
    justify-content: center;
  }
  .tagline {
    font-family: "Lexend", sans-serif;
    font-weight: 600;
    font-size: 14px;
    letter-spacing: 1px;
    text-transform: uppercase;
    color: #fff;
  }
  .social-row {
    position: absolute;
    left: 0;
    right: 0;
    top: 260px;
    display: flex;
    justify-content: center;
    gap: 14px;
  }
  .social-dot {
    width: 24px;
    height: 24px;
    border-radius: 50%;
    background: var(--brand-red);
  }
</style>
</head>
<body>

  <section class="card card--front">
    <h1 class="brand-name">Brightwire<br>Hollow</h1>
  </section>

  <section class="card card--back">
    <span class="corner-accent"></span>
    <h2 class="holder-name">Marcus Pell</h2>
    <span class="divider"></span>
    <ul class="contact-list">
      <li class="contact-item contact-item--phone">
        <svg class="contact-icon" viewBox="0 0 24 24" aria-hidden="true"><path fill="#e8321f" d="M6.6 10.8a15.1 15.1 0 0 0 6.6 6.6l2.2-2.2a1 1 0 0 1 1-.25 11.4 11.4 0 0 0 3.6.57 1 1 0 0 1 1 1V20a1 1 0 0 1-1 1A17 17 0 0 1 3 4a1 1 0 0 1 1-1h3.5a1 1 0 0 1 1 1c0 1.25.2 2.45.57 3.6a1 1 0 0 1-.25 1z"/></svg>
        0431 587 219
      </li>
      <li class="contact-item">
        <svg class="contact-icon" viewBox="0 0 24 24" aria-hidden="true"><rect x="2" y="5" width="20" height="14" rx="2" fill="#e8321f"/><path d="M2.5 6l9.5 7 9.5-7" fill="none" stroke="#1d1c1c" stroke-width="1.6"/></svg>
        marcus@brightwirehollow.com.au
      </li>
      <li class="contact-item">
        <svg class="contact-icon" viewBox="0 0 24 24" aria-hidden="true"><g fill="none" stroke="#e8321f" stroke-width="1.8"><circle cx="12" cy="12" r="9.5"/><ellipse cx="12" cy="12" rx="4.2" ry="9.5"/><path d="M2.5 12h19M4 7h16M4 17h16"/></g></svg>
        brightwirehollow.com.au
      </li>
    </ul>
    <div class="tagline-band">
      <p class="tagline">24/7 Sydney Electrician</p>
    </div>
    <div class="social-row">
      <span class="social-dot" role="img" aria-label="Social profile link"></span>
      <span class="social-dot" role="img" aria-label="Social profile link"></span>
    </div>
  </section>

</body>
</html>
```